Fatigued and Overloaded by COVID Messages? We need original illustrations to show that.

Everywhere you look there are messages about COVID. That is leading many people to feel fatigued and overloaded by the messages.

We surveyed U.S. adults March 20th - 24th, 2020 and measured message fatigue, information overload, perceived repetition, and perceived exaggeration. Here is how participants responded:

When it comes to coronavirus . . .
55% feel exhausted by all the messages.
54% feel overloaded by the amount of information.
51% feel that the messages are repetitive.
47% feel like messages exaggerate how bad it is.

In other words, almost half of U.S. adults show signs of message fatigue, information overload, perceived message repetition, and perceived message exaggeration.

We will continue to survey 400 adults every week for the next 16 weeks. Each time we will measure message fatigue, information overload, perceived repetition, and perceived exaggeration. We expect that it will increase over time.

What are we looking for? We need innovative and original illustrations that attempt to communicate these findings. The illustrations would visualize message fatigue, information overload, perceived message repetition, and perceived message exaggeration.

What sort of visual are we looking for? Our preference is for an original illustration (or set of illustrations). Our preference is for creative and powerful illustrations, but we are also open to the creative and well-executed infographics.

We need these images fast . We will award monetary prizes to the 3 best designs. If we like more than that, then we might purchase more (e.g., in past contests, we have purchased as many as 30 designs).

What we will need:
(1) The illustrations must be original and we will need the photoshop and/or illustrator files for all artwork. (By original, we mean that the illustrations are 100% created by you. Our organization requires that we utilize only original illustrated work. We have had issues with free imagery being pirated and reposted as free. We sidestep that issue by just having everything created.)

(2) The illustration should say, somewhere: "Based on a survey of 400 U.S. adults conducted March 20 - 24th, 2020."

(3) We will have almost 4 months worth of data by the time this is done. In other words, the illustrations might be able to help us present that weekly data.

(4) We have conducted other Artvendo projects. It might be helpful to examine designs we liked in the past. For example, here is another COVID project we just finished:

https://jobs.artvendo-example.com/job/5162048

Target Market(s)

U.S. adults

Requirements
Must have
• Original illustrations. Mobile friendly design. People will view this on their smartphones.
Nice to have
• A design that we can use to communicate the data across time.

```html
<!DOCTYPE html>
<html lang="en">
<head>
<meta charset="utf-8">
<title>How people feel with COVID-19 messages and information</title>
<link rel="stylesheet" href="https://fonts.googleapis.com/css2?family=Fjalla+One&family=Bree+Serif&family=Fira+Sans+Condensed:wght@600&family=Open+Sans:wght@600;700&display=swap">
<style>
  :root {
    --mint: #4dfcd0;
    --mint-low: #86f7a8;
    --ink: #1a1a1a;
    --magenta: #e8107e;
    --navy: #223d58;
    --navy-deep: #0f1c2b;
    --silver: #c9c9c9;
    --red: #ee3a3a;
    --orange: #f2582a;
    --amber: #f9a83a;
    --yellow: #f8e61c;
    --globe: #3f8fd6;
    --globe-light: #7cc4f0;
    --ground: #f5961f;
    --horn: #ef2a62;
    --horn-light: #f58fb0;
  }
  html, body { margin: 0; padding: 0; overflow: hidden; }
  body { width: 1200px; height: 752px; }
  .canvas {
    position: relative; width: 1200px; height: 752px; overflow: hidden;
    background: linear-gradient(180deg, var(--mint) 0%, #55fbc4 60%, var(--mint-low) 100%);
  }
  .mascot-art {
    position: absolute; left: 14px; top: 18px; width: 356px; height: 515px;
    border-radius: 28px;
    background: linear-gradient(180deg, var(--globe-light) 0%, var(--globe) 55%, #5aa7e6 82%, var(--ground) 82%, var(--ground) 100%);
  }
  .megaphone-art {
    position: absolute; left: 1000px; top: 70px; width: 200px; height: 190px;
    border-radius: 24px 0 0 24px;
    background: linear-gradient(135deg, var(--horn-light) 0%, var(--horn) 100%);
  }
  .headline {
    position: absolute; left: 490px; top: 38px; margin: 0;
    font-family: "Fjalla One", sans-serif; font-weight: 400; color: var(--ink);
    line-height: 1;
  }
  .headline .lead { display: block; font-size: 46px; }
  .headline .topic {
    display: block; font-size: 100px; color: var(--magenta); margin: 12px 0 0 -3px;
    letter-spacing: 4px;
    -webkit-text-stroke: 3px #fff; paint-order: stroke fill;
  }
  .headline .tail { display: block; font-size: 46px; margin-top: -2px; }
  .stats-panel {
    position: absolute; left: 430px; top: 276px; width: 800px; height: 500px;
    border-radius: 52px 0 0 0; background: var(--silver);
  }
  .stats-panel .inner {
    position: absolute; left: 8px; top: 21px; right: 0; bottom: 0;
    border-radius: 46px 0 0 0;
    background: radial-gradient(ellipse at 40% 45%, var(--navy) 0%, var(--navy-deep) 100%);
  }
  .stat {
    position: absolute; left: 44px; height: 100px; display: flex; align-items: center;
  }
  .stat .value {
    font-family: "Fira Sans Condensed", sans-serif; font-weight: 600;
    font-size: 92px; width: 142px; line-height: 1; white-space: nowrap;
  }
  .stat .value small { font-size: 42px; margin-left: 2px; }
  .stat .label { font-family: "Bree Serif", serif; font-size: 34px; line-height: 43px; }
  .s1 { top: 4px; color: var(--red); }
  .s2 { top: 110px; color: var(--orange); }
  .s3 { top: 217px; color: var(--amber); }
  .s4 { top: 326px; color: var(--yellow); }
  .survey-note {
    position: absolute; left: 27px; top: 565px; margin: 0;
    font-family: "Open Sans", sans-serif; font-weight: 700; font-size: 21px;
    line-height: 25px; color: var(--ink);
  }
  .finding {
    position: absolute; left: 28px; top: 633px; margin: 0;
    font-family: "Open Sans", sans-serif; font-weight: 600; font-size: 19.5px;
    line-height: 21.5px; color: var(--magenta);
  }
</style>
</head>
<body>
<main class="canvas">
  <div class="mascot-art" role="img" aria-label="Cartoon globe wearing a face mask, raising a hand to stop, standing on an orange spot among virus particles"></div>
  <div class="megaphone-art" role="img" aria-label="Red megaphone blasting virus particles"></div>

  <h1 class="headline">
    <span class="lead">How people feel with</span>
    <span class="topic">COVID-19</span>
    <span class="tail">messages and information?</span>
  </h1>

  <section class="stats-panel">
    <div class="inner">
      <div class="stat s1"><span class="value">55<small>%</small></span><span class="label">Exhausted by all the messages.</span></div>
      <div class="stat s2"><span class="value">54<small>%</small></span><span class="label">Overloaded by the amount<br>of information.</span></div>
      <div class="stat s3"><span class="value">51<small>%</small></span><span class="label">The messages are repetitive.</span></div>
      <div class="stat s4"><span class="value">47<small>%</small></span><span class="label">Messages exaggerate<br>how bad it is.</span></div>
    </div>
  </section>

  <p class="survey-note">Based on a survey of 400 U.S. adults<br>conducted March 20 - 24th, 2020</p>
  <p class="finding">Almost half of U.S. adults show signs<br>of message fatigue, information overload,<br>perceived message repetition,<br>and perceived message exaggeration.</p>
</main>
</body>
</html>
```